Pop-up Banner

Would like a design for a pop-up 85 x 206cm banner for a trade show. (from nordel press)
We would like "our logo" (copperline ventures) - then the tagline - "Your Trusted Partner in Data-Driven Decisions"
*Supporting Bullets*
Unified data, analytics & AI
Trusted insights, faster outcomes
Real-time intelligence at scale
Enterprise-ready, secure solutions
Clarity from data complexity
trusted by...some company logos
Partners with : partner logo
Our Colours: #FFA300, #3D4176, #FDD16E, #F87C57, #A68118, #1C2F36

```html
<!DOCTYPE html>
<html lang="en">
<head>
<meta charset="utf-8">
<title>Copperline Ventures – Pop-up Banner</title>
<link rel="stylesheet" href="https://fonts.googleapis.com/css2?family=Barlow+Condensed:wght@700&family=Montserrat:wght@500;600;700&display=swap">
<style>
  :root {
    --orange: #FFA300;
    --navy: #3D4176;
    --sand: #FDD16E;
    --coral: #F87C57;
    --bronze: #A68118;
    --ink: #1C2F36;
    --page: #e6e7ea;
    --mist: #eef2f8;
  }
  * { margin: 0; padding: 0; box-sizing: border-box; }
  html, body { width: 800px; height: 1200px; overflow: hidden; }
  body { background: var(--page); font-family: "Montserrat", sans-serif; position: relative; }

  .banner {
    position: absolute; left: 153px; top: 17px;
    width: 494px; height: 1166px; overflow: hidden;
    background: linear-gradient(180deg, #ffffff 0%, #ffffff 55%, #e4ebf6 80%, #dbe3f2 100%);
  }
  .banner-art { position: absolute; inset: 0; }

  .brand { position: absolute; left: 46px; top: 66px; display: flex; align-items: center; gap: 14px; }
  .brand-dot { width: 54px; height: 54px; border-radius: 50%; background: var(--orange); }
  .brand-name {
    color: var(--orange); font-weight: 700; font-size: 20px; line-height: 23px; letter-spacing: 0.5px;
  }

  .tagline {
    position: absolute; left: 59px; top: 340px;
    font-family: "Barlow Condensed", sans-serif; font-weight: 700;
    color: #fff; font-size: 41px; line-height: 47px;
  }

  .benefits { position: absolute; left: 109px; top: 596px; list-style: none; }
  .benefits li {
    height: 55.4px; line-height: 24px;
    color: var(--navy); font-weight: 600; font-size: 15.7px;
  }

  .logo-panel {
    position: absolute; left: 62px; width: 370px; height: 96px;
    border-radius: 10px; padding: 2px;
    background: linear-gradient(100deg, var(--orange), var(--sand) 40%, #c9cbe0 65%, var(--navy));
  }
  .logo-panel-inner {
    width: 100%; height: 100%; border-radius: 8px;
    background: rgba(255,255,255,0.9); position: relative;
  }
  .logo-panel.trusted { top: 872px; }
  .logo-panel.partners { top: 985px; }
  .panel-title {
    position: absolute; top: 12px; left: 0; right: 0; text-align: center;
    color: var(--navy); font-weight: 700; font-size: 11px; letter-spacing: 0.4px;
  }
  .logo-name {
    position: absolute; transform: translateX(-50%);
    white-space: nowrap; font-weight: 600; font-size: 12.5px; color: var(--navy);
  }

  .footer-band {
    position: absolute; left: 0; bottom: 0; width: 494px; height: 66px;
    background: var(--orange);
    display: flex; align-items: center; justify-content: center;
  }
  .footer-url { color: #fff; font-weight: 700; font-size: 17px; letter-spacing: 0.2px; }
</style>
</head>
<body>
<main class="banner">
  <svg class="banner-art" viewBox="0 0 494 1166" width="494" height="1166" aria-hidden="false">
    <defs>
      <linearGradient id="photoTone" x1="0" y1="0" x2="1" y2="1">
        <stop offset="0" stop-color="#f4f6fa"/>
        <stop offset="0.55" stop-color="#dfe8f0"/>
        <stop offset="1" stop-color="#e9ddd0"/>
      </linearGradient>
      <linearGradient id="navyBand" x1="0" y1="0" x2="0" y2="1">
        <stop offset="0" stop-color="#3D4176"/>
        <stop offset="0.6" stop-color="#4b4f86"/>
        <stop offset="1" stop-color="#7d80a8"/>
      </linearGradient>
      <linearGradient id="stripeTop" x1="0" y1="0" x2="1" y2="1">
        <stop offset="0" stop-color="#A68118"/>
        <stop offset="1" stop-color="#FFA300"/>
      </linearGradient>
      <linearGradient id="stripeBottom" x1="0" y1="0" x2="1" y2="1">
        <stop offset="0" stop-color="#FFA300"/>
        <stop offset="1" stop-color="#FDD16E"/>
      </linearGradient>
    </defs>

    <rect class="hero-photo" x="124" y="29" width="370" height="420" fill="url(#photoTone)"
          role="img" aria-label="Photo of a presenter holding a tablet beside a screen showing a bar chart"/>
    <polygon class="hero-frame" points="401,79 474,121 474,205 401,247 328,205 328,121"
             fill="none" stroke="#FFA300" stroke-width="5"/>

    <path class="navy-band" fill="url(#navyBand)"
          d="M0,179 L72,179 Q96,179 112,195 L236,319 Q245,328 258,328 L405,328 Q419,328 429,338 L494,403
             L494,558 L135,558 Q112,558 96,544 L0,465 Z"/>
    <path class="stripe-top" fill="url(#stripeTop)"
          d="M0,173 L0,232 L83,313 Q90,320 100,320 L154,320 L10,176 Z"/>
    <path class="stripe-bottom" fill="url(#stripeBottom)"
          d="M314,449 L396,449 Q414,449 428,463 L494,529 L494,620 Z"/>

    <line class="timeline" x1="60" y1="525" x2="60" y2="600" stroke="#5a4e5e" stroke-width="2.5"/>
    <line class="timeline" x1="60" y1="600" x2="60" y2="829" stroke="#FFA300" stroke-width="3"/>

    <g class="benefit-icons" fill="none" stroke="#fff" stroke-width="1.4" stroke-linecap="round" stroke-linejoin="round">
      <circle cx="60" cy="608" r="20" fill="#FFA300" stroke="none"/>
      <rect x="51" y="599" width="18" height="18" rx="2"/>
      <path d="M54,595v4M58,595v4M62,595v4M66,595v4M54,617v4M58,617v4M62,617v4M66,617v4M54,612l4-4 3,3 5-6"/>

      <circle cx="60" cy="663" r="20" fill="#3D4176" stroke="none"/>
      <path d="M55,664a7,7 0 1 1 10,0c-1.5,1.5-2,3-2,4h-6c0-1-0.5-2.5-2-4z M57,671h6M57.5,674h5 M57,659l2.5,2.5 4-4" stroke="#FFA300"/>

      <circle cx="60" cy="718" r="20" fill="#FFA300" stroke="none"/>
      <rect x="49" y="709" width="22" height="17" rx="2"/>
      <path d="M49,713h22M52,722l5-4 4,3 6-5"/>
      <circle cx="69" cy="725" r="3.5" fill="#FFA300"/>

      <circle cx="60" cy="773" r="20" fill="#3D4176" stroke="none"/>
      <path d="M60,761l6,2v4c0,3.5-2.5,6-6,7c-3.5-1-6-3.5-6-7v-4z M57.5,767l2,2 3.5-3.5 M50,785c0-4 3-6 5-6s5,2 5,6 M60,785c0-4 3-6 5-6s5,2 5,6" stroke="#FFA300"/>

      <circle cx="60" cy="829" r="20" fill="#FFA300" stroke="none"/>
      <circle cx="60" cy="829" r="3.5"/>
      <circle cx="52" cy="821" r="3"/><circle cx="68" cy="821" r="3"/>
      <circle cx="52" cy="837" r="3"/><circle cx="68" cy="837" r="3"/>
      <path d="M54.5,823.5l3,3M65.5,823.5l-3,3M54.5,834.5l3-3M65.5,834.5l-3-3"/>
    </g>
  </svg>

  <div class="brand">
    <span class="brand-dot"></span>
    <p class="brand-name">COPPERLINE<br>VENTURES</p>
  </div>

  <h1 class="tagline">Your Trusted<br>Partner in Data-Driven<br>Decisions</h1>

  <ul class="benefits">
    <li>Unified data, analytics &amp; AI</li>
    <li>Trusted insights, faster outcomes</li>
    <li>Real-time intelligence at scale</li>
    <li>Enterprise-ready, secure solutions</li>
    <li>Clarity from data complexity</li>
  </ul>

  <section class="logo-panel trusted">
    <div class="logo-panel-inner">
      <h2 class="panel-title">TRUSTED BY</h2>
      <span class="logo-name" style="left:82px;top:36px">Halden</span>
      <span class="logo-name" style="left:188px;top:36px">Kestrel Harbour</span>
      <span class="logo-name" style="left:290px;top:36px">Varnel</span>
      <span class="logo-name" style="left:140px;top:62px">Brightwell</span>
      <span class="logo-name" style="left:231px;top:62px">Ostara</span>
    </div>
  </section>

  <section class="logo-panel partners">
    <div class="logo-panel-inner">
      <h2 class="panel-title">PARTNERS WITH</h2>
      <span class="logo-name" style="left:86px;top:38px">Tessaro</span>
      <span class="logo-name" style="left:190px;top:38px">Quorvia</span>
      <span class="logo-name" style="left:290px;top:38px">Ledgeris</span>
      <span class="logo-name" style="left:188px;top:62px">Clearpath Data</span>
    </div>
  </section>

  <footer class="footer-band">
    <p class="footer-url">copperlineventures.com</p>
  </footer>
</main>
</body>
</html>
```